Create a Graphic About YOURSELF and PixelHarbor

PixelHarbor would like you (designers) to create an awesome graphic to promote YOURSELF and your profile on PixelHarbor!

Your graphic should communicate your name, your services and should mention PixelHarbor.

The design should be perfect for sharing on Chatterly. Here's an example of what we'd like http://blog.pixelharbor-example.ca/article/333/pixelharbor-launches-3000-hire-me-social-design-contest

Once you submitted your design, we'd love you to share the design ('advertisement') and promote yourself and PixelHarbor to your friends and potential customers. So make your submissions great and get your friends to vote for your design by 'Liking' it on Chatterly!

Prizes:
$1500 - "PixelHarbor Community" prize awarded to the designer with the most Chatterly 'Likes'
5 x $50 for the next 5 'most liked' designs on Chatterly

$1000 - "Hire Me" prize awarded to the designer who receives the most client invites
5 x $50 for the next 5 'most invited' designers

In summary, this is a great opportunity for you to increase your exposure to PixelHarbor customers and win cash prizes. Show off your design skills and get hired by PixelHarbor customers from around the world!

Target Market(s)

Fans, friends and customers of YOU

Industry/Entity Type

Cash

Requirements
Must have
• 1) Include your PixelHarbor user name on the graphic so customers can find you in the PixelHarbor Designer Directory
2) Include the tagline "Hire Me on PixelHarbor.com!" in your graphic design.
3) Share your design's URL on our Chatterly wall at http://chatterly-example.com/pixelharbor and get your friends to 'like' your design.
Nice to have
• 1) Include a tagline that expresses your design approach/philosophy
2) Artwork dimensions: 403 x 403 px
3) You can submit more than 1 design!
Should not have
• You must own the copyright of any images you use including stock imagery.

```html
<!DOCTYPE html>
<html lang="en">
<head>
<meta charset="utf-8">
<title>Need Design? Hire Me on PixelHarbor</title>
<link rel="stylesheet" href="https://fonts.googleapis.com/css2?family=Open+Sans:wght@700;800&display=swap">
<style>
  :root {
    --slate: #6d6e71;
    --paper: #ffffff;
    --font-main: "Open Sans", Arial, sans-serif;
  }
  html, body {
    margin: 0;
    padding: 0;
    width: 1200px;
    height: 1200px;
    overflow: hidden;
    background: var(--slate);
  }
  .poster {
    position: relative;
    width: 1200px;
    height: 1200px;
    background: var(--slate);
    font-family: var(--font-main);
    font-weight: 700;
    color: var(--paper);
  }
  .rule {
    position: absolute;
    left: 150px;
    width: 897px;
    height: 4px;
    background: var(--paper);
  }
  .rule--top { top: 267px; }
  .rule--bottom { top: 838px; }
  .headline {
    position: absolute;
    margin: 0;
    line-height: 1;
    white-space: nowrap;
  }
  .headline--need {
    left: 146px;
    top: 266px;
    font-size: 218px;
    letter-spacing: 0.08em;
  }
  .headline--design {
    left: 146px;
    top: 462px;
    font-size: 180px;
  }
  .question-mark {
    position: absolute;
    left: 826px;
    top: 236px;
    font-size: 420px;
    font-weight: 800;
    line-height: 1;
    transform: rotate(8deg);
    transform-origin: 50% 60%;
  }
  .hire-box {
    position: absolute;
    left: 183px;
    top: 671px;
    width: 681px;
    height: 158px;
    background: var(--paper);
  }
  .hire-text {
    position: absolute;
    left: 196px;
    top: 665px;
    margin: 0;
    font-size: 160px;
    line-height: 1;
    color: var(--slate);
    white-space: nowrap;
  }
  .headline--on {
    left: 196px;
    top: 827px;
    font-size: 171px;
  }
  .brand-dot {
    position: absolute;
    left: 468px;
    top: 866px;
    width: 110px;
    height: 110px;
    border-radius: 50%;
    background: var(--paper);
  }
  .brand-site {
    position: absolute;
    left: 592px;
    top: 884px;
    margin: 0;
    font-size: 31px;
    line-height: 1.2;
    white-space: nowrap;
  }
  .username {
    position: absolute;
    left: 590px;
    top: 920px;
    margin: 0;
    padding: 0 6px;
    background: var(--paper);
    color: var(--slate);
    font-size: 25px;
    line-height: 28px;
    white-space: nowrap;
  }
</style>
</head>
<body>
  <main class="poster">
    <div class="rule rule--top"></div>
    <h1 class="headline headline--need">NEED</h1>
    <p class="headline headline--design">DESIGN</p>
    <span class="question-mark">?</span>
    <div class="hire-box"></div>
    <p class="hire-text">HIRE ME</p>
    <div class="rule rule--bottom"></div>
    <p class="headline headline--on">ON</p>
    <div class="brand-dot"></div>
    <p class="brand-site">PixelHarbor.com</p>
    <p class="username">Marek.Volkonsky</p>
  </main>
</body>
</html>
```